Im open to ideas.. I was thinking on my business cards aswell as my logo. a place for my name. email. phone number and abn..

ive attched a file with my business logo. which i dont love the colours.. i was think a dark background with charcoal letters so something along those colour schumes but im open to ideas..

Industry/Entity Type

Business

Logo Text

RLB Constructions

```html
<!DOCTYPE html>
<html lang="en">
<head>
<meta charset="utf-8">
<title>RLB Constructions – Business Card</title>
<link href="https://fonts.googleapis.com/css2?family=Open+Sans:wght@400;600;700&display=swap" rel="stylesheet">
<style>
  :root {
    --page-bg: #e4e1dd;
    --card-light: #d6d6d6;
    --card-dark: #555555;
    --wave-line: #1c1c1c;
    --ink: #4a4a4a;
    --ink-soft: #5a5a5a;
    --on-dark: #ececec;
  }
  html, body {
    margin: 0;
    width: 1200px;
    height: 900px;
    overflow: hidden;
    background: var(--page-bg);
    font-family: "Open Sans", Arial, sans-serif;
  }
  .card {
    position: absolute;
    left: 180px;
    top: 191px;
    width: 840px;
    height: 518px;
    background: var(--card-light);
    overflow: hidden;
    box-shadow: 0 6px 24px rgba(0,0,0,0.18);
  }
  .card__wave {
    position: absolute;
    inset: 0;
    width: 100%;
    height: 100%;
  }
  .holder {
    position: absolute;
    right: 54px;
    top: 52px;
    text-align: right;
    color: var(--ink);
  }
  .holder__name {
    margin: 0;
    font-size: 31px;
    font-weight: 600;
    line-height: 1.15;
  }
  .holder__title {
    margin: 2px 0 0;
    font-size: 20px;
    font-weight: 400;
    color: var(--ink-soft);
  }
  .brand {
    position: absolute;
    left: 48px;
    top: 196px;
    margin: 0;
    font-size: 44px;
    font-weight: 700;
    color: var(--ink);
    letter-spacing: 0.5px;
  }
  .abn {
    position: absolute;
    left: 147px;
    top: 322px;
    margin: 0;
    font-size: 20px;
    color: var(--ink);
  }
  .abn strong { font-weight: 700; }
  .contact {
    position: absolute;
    right: 54px;
    top: 350px;
    margin: 0;
    padding: 0;
    list-style: none;
    color: var(--on-dark);
    font-size: 20px;
  }
  .contact__item {
    display: flex;
    justify-content: flex-end;
    align-items: center;
    gap: 10px;
    height: 31px;
  }
  .contact__icon {
    width: 15px;
    height: 15px;
    fill: var(--on-dark);
  }
</style>
</head>
<body>
  <div class="card">
    <svg class="card__wave" viewBox="0 0 652 402" preserveAspectRatio="none" aria-hidden="true">
      <path d="M0,268 C90,316 170,350 240,345 C330,338 400,215 520,196 C590,186 630,212 652,238 L652,402 L0,402 Z" fill="var(--card-dark)"/>
      <path d="M0,252 C90,302 170,336 240,331 C330,324 400,200 520,181 C590,171 630,198 652,224" fill="none" stroke="var(--wave-line)" stroke-width="5"/>
    </svg>

    <div class="holder">
      <p class="holder__name">Daniel Hartley</p>
      <p class="holder__title">Managing Director</p>
    </div>

    <p class="brand">RLB Constructions</p>

    <p class="abn"><strong>ABN:</strong>7654321</p>

    <ul class="contact">
      <li class="contact__item">044-987 654 321
        <svg class="contact__icon" viewBox="0 0 16 16"><path d="M1 6c0-2 3-4 7-4s7 2 7 4v1h-3.5V5.5h-7V7H1zM4 8h8l2 5H2z"/></svg>
      </li>
      <li class="contact__item">info@rlbbuild.com
        <svg class="contact__icon" viewBox="0 0 16 16"><path d="M1 3h14v10H1z M2.5 4.5 8 9l5.5-4.5" fill="var(--on-dark)" stroke="var(--card-dark)" stroke-width="1.2"/></svg>
      </li>
      <li class="contact__item">www.rlbbuild.com
        <svg class="contact__icon" viewBox="0 0 16 16"><circle cx="8" cy="8" r="7"/><path d="M5 4c2 1 1 3 3 3s1 3 3 4M9 3c1 1 3 1 3 3" fill="none" stroke="var(--card-dark)" stroke-width="1.3"/></svg>
      </li>
    </ul>
  </div>
</body>
</html>
```